KRV Anti-Money Laundering Postcard

We are a U.S. based regulatory compliance consulting company who services the financial industry (stock, bonds, equities, banking, etc.)

One of the services that we offer is Independent Anti-Money Laundering audit reviews. These reviews are required by U.S. law for certain financial institutions.

We are looking for a 6" x 8.5" horizontally oriented postcard to market our services in this business. The card should be sharp and professional.

The font and back of the card must have our logo and include

"Anti-Money Laundering Compliance" or "Anti-Money Laundering Compliance Services"

We would like the following message to be included on the card either on the front or preferably the back:

"Belwick & Associates are specialists in Anti-Money Laundering compliance. Our firm’s Anti-Money Laundering compliance solutions include:

• Independent Money Laundering Audits
• Anti-Money Laundering Compliance Procedures
• Anti-Money Laundering Training

Let our expert compliance team assist you in ensuring that your firm is compliant with all of its money laundering and other compliance obligations.

The back of the card should have our address, website, phone number and website: The address is normally included in the return address section noted in the Post Office requirements section blow.

42 W. Calloway Street, Suite 300
Pasadena, CA 91101
(877) 318-4092
info@belwickandassociates.example
www.belwickandassociates.example

Back of the postcard Post Office Design requirements:

http://www.quillmailprint.example/products/postcard-deluxe

Target Market(s)

Stock Brokerage Firms, Investment Advisers, Banks and other financial institutions

Industry/Entity Type

Financial Planning

Font styles to use
Sans Serif

Requirements
Must have
• Our Logo on the front and back. Clean and professional. Nice artwork.

```html
<!DOCTYPE html>
<html lang="en">
<head>
<meta charset="utf-8">
<title>Belwick & Associates — Anti-Money Laundering Postcard</title>
<link href="https://fonts.googleapis.com/css2?family=Arimo:wght@400&family=Cabin:wght@400;500&display=swap" rel="stylesheet">
<style>
  :root {
    --backdrop: #c8d5bc;
    --charcoal: #333333;
    --slate: #2f3337;
    --paper: #e2e2e2;
    --box-fill: #d8d8dc;
    --box-edge: #b9b9bf;
    --accent-red: #a11b1f;
    --white: #ffffff;
    --ink: #111111;
  }
  * { box-sizing: border-box; margin: 0; padding: 0; }
  html, body { width: 1200px; height: 1200px; overflow: hidden; }
  body { background: var(--backdrop); position: relative; font-family: "Arimo", Arial, sans-serif; }

  .postcard { position: absolute; top: 407px; width: 548px; height: 354px; overflow: hidden; }
  .postcard--front { left: 46px; background: var(--paper); }
  .postcard--back { left: 615px; background: var(--paper); }

  /* Front */
  .front-header { position: absolute; left: 0; top: 0; width: 548px; height: 229px; background: var(--charcoal); }
  .brand { position: absolute; display: flex; align-items: center; gap: 10px; font-family: "Cabin", sans-serif; font-weight: 500; white-space: nowrap; }
  .brand__mark { width: 22px; height: 22px; flex: none; }
  .front-header .brand { left: 150px; top: 36px; color: var(--white); font-size: 26px; letter-spacing: 0.5px; }
  .front-header .brand__mark { background: var(--white); }

  .service-badge { position: absolute; left: 410px; top: 71px; width: 120px; height: 120px; }
  .service-badge svg { position: absolute; inset: 0; }
  .service-badge__title { position: absolute; inset: 0; display: flex; align-items: center; justify-content: center; text-align: center; font-family: "Cabin", sans-serif; color: var(--white); font-size: 16px; line-height: 20px; }

  .intro { position: absolute; left: 23px; top: 186px; color: var(--white); font-size: 10.4px; line-height: 16px; }

  .solutions { position: absolute; left: 23px; top: 237px; display: flex; gap: 5px; list-style: none; }
  .solution { width: 165px; height: 70px; background: var(--box-fill); border: 1px solid var(--box-edge); border-top: 2px solid var(--accent-red); text-align: center; padding-top: 10px; font-size: 13.4px; line-height: 16px; color: var(--ink); }

  .cta { position: absolute; left: 25px; top: 317px; width: 500px; height: 20px; background: var(--accent-red); border-radius: 8px; color: var(--white); font-size: 8px; line-height: 8.5px; text-align: center; padding-top: 1.5px; }

  /* Back */
  .return-address { position: absolute; left: 0; top: 0; width: 250px; height: 156px; background: var(--slate); padding: 30px 0 0 14px; font-family: "Cabin", sans-serif; color: var(--white); font-size: 14px; line-height: 21px; font-style: normal; white-space: nowrap; }
  .postcard--back .brand { left: 38px; top: 230px; color: var(--ink); font-size: 24px; }
  .postcard--back .brand__mark { background: var(--ink); }
</style>
</head>
<body>

<section class="postcard postcard--front">
  <div class="front-header">
    <div class="brand"><span class="brand__mark"></span><span class="brand__name">Belwick &amp; Associates</span></div>

    <div class="service-badge">
      <svg viewBox="0 0 120 120" aria-hidden="true">
        <polyline points="45,18 60,3 75,18" fill="none" stroke="#fff" stroke-width="1"/>
        <polyline points="45,102 60,117 75,102" fill="none" stroke="#fff" stroke-width="1"/>
        <polyline points="11,48 1,60 11,72" fill="none" stroke="#fff" stroke-width="1"/>
        <polyline points="109,48 119,60 109,72" fill="none" stroke="#fff" stroke-width="1"/>
      </svg>
      <p class="service-badge__title">Anti-Money<br>Laundering<br>Compliance<br>Services</p>
    </div>

    <p class="intro">Belwick &amp; Associates are specialists in Anti-Money Laundering compliance.<br>Our firm’s Anti-Money Laundering compliance solutions include:</p>
  </div>

  <ul class="solutions">
    <li class="solution">Independent Money<br>Laundering Audits</li>
    <li class="solution">Anti-Money Laundering<br>Compliance<br>Procedures</li>
    <li class="solution">Anti-Money<br>Laundering Training</li>
  </ul>

  <p class="cta">Let our expert compliance team assist you in ensuring that your firm is compliant with all of its money laundering and<br>other compliance obligations</p>
</section>

<section class="postcard postcard--back">
  <address class="return-address">
    42 W. Calloway Street, Suite 300<br>
    Pasadena, CA 91101<br>
    (877) 318-4092<br>
    info@belwickandassociates.example<br>
    www.belwickandassociates.example
  </address>
  <div class="brand"><span class="brand__mark"></span><span class="brand__name">Belwick &amp; Associates</span></div>
</section>

</body>
</html>
```